Velmora Resident Safety and Security

Need a website for our company. Please see attached outlines and files
Main Page
Velmora
Design – Install – Maintain
Supporting the Safety and Security needs of your Community
Best in Class Systems for the Safety and Security of your Residents and Staff
Your Trusted Advisor
Solutions
Systems tailored to the needs of your facility
Skilled Nursing Facilities
Long Term Care
CCRC’s
Assisted Living
Independent Living
Access Control
Maglocks
Keypads
Prox readers (key fob, card, etc.)
Wireless locks
Multi-Tennant
Perimeter doors
Resident Apartment doors
Nurse Call
Tone / Visual
Fixed Stations
Dome Lights
T/V+ Audio
Fixed Stations
Dome Lights
Audio communication
Wireless
Fixed Stations
Resident Pendants
Hybrid Systems
Wired and Wireless integrated for seamless notification and reporting.
CCTV
Surveillance systems to fit your security needs and your budget
Remote Access, Local or Cloud Storage
Good, Better, Best proposals
Wander management
Door Alarming
Detection of wandering resident
Remote alarming and alerts
Delay elopement to allow for redirection
Network Infrastructure
Modern infrastructure for modern systems
Conference and Telepresence
Professionally installed systems to allow for seamless clear communications between teams across infinite distances.
Our Team
Rolf Amundsen – President
Patricia Lowell – Vice President of Customer Success
Miles Forbush – Account Executive
Industry Associations
Harborline Collective
Massachusetts chapter of the National Guild of Elder Care Stewards
Contact Us
Phone (603) 555-0172
Email Info@Velmora.example
Facilities we serve
Independent Senior Living
Assisted Living
Memory Care
CCRC (Continuing Care Retirement Community)
Skilled Nursing / Rehab
Multi-Tenant
Outpatient Surgical Centers
Endoscopy Clinics
Acute Care
Urgent Care
Commercial Properties of all types
General notes
Imagery should invoke high tech, safety, security and include healthcare themes. the circuit board shield is our logo and a ghosted image as back ground or some animation that brings in the logo or the circuit board should be incorporated.
Velmora is a systems integration company specializing in low voltage solutions for healthcare facilities and senior living communities. The company aims to leverage its industry expertise, and innovative products to become the market leader in systems integration, focusing on enhancing safety and operational efficiency.
Vision and Mission: Velmora’s vision is to revolutionize integrated systems within healthcare and commercial environments by delivering innovative, reliable, and tailored solutions that enhance operational efficiency and patient care. The company is committed to setting new standards for resident safety and customer satisfaction.
Company Summary: Founded by experienced industry professionals, Velmora specializes in the design, installation, and maintenance of systems including Access Control, Nurse Call, Delayed Egress, network infrastructure, and overhead paging primarily for healthcare clients.
Products and Services: The company offers a comprehensive range of low voltage systems including Nurse Call (wired and wireless), Wander Management, Access Control, and wired/wireless network infrastructure tailored for senior living and healthcare facilities.
Mission Statement
Velmora was founded to fill a specific need. Senor living communities and healthcare facilities of all kinds face unique challenges in regards to technology and systems integration. Velmora is perfectly positioned with an experienced management team, skilled technicians, industry relationships with suppliers and facility management groups. We have built our reputation on excellent customer service and the highest standards of integrity. Velmora’s vision is to revolutionize integrated systems within healthcare and commercial environments by delivering innovative, reliable, and tailored solutions that enhance operational efficiency and patient care. We are committed to setting new standards for resident safety and customer satisfaction in every project we undertake.

Target Market(s)

Senior living communities staff and management

Industry/Entity Type

Systems Intergration

Coding

Coded - Design and coding required

Font styles to use
Serif
Sans Serif

Colors
0054AA
0677BA
7BADD7
CADEEF
E8F1F8
0094D4
00A9DD
6FCCEA
C7EBF8
E9F6FB

Requirements
Must have
• unique eye catching design including circuit board (PCB) type design and our supplied logo files

```html
<!DOCTYPE html>
<html lang="en">
<head>
<meta charset="utf-8">
<title>Velmora Resident Safety and Security</title>
<link rel="stylesheet" href="https://fonts.googleapis.com/css2?family=Inter:wght@300;400;500;600;700&family=Playfair+Display:wght@600;700&display=swap">
<style>
:root{
  --blue:#0054AA;
  --blue-2:#0677BA;
  --blue-soft:#7BADD7;
  --blue-pale:#CADEEF;
  --blue-mist:#E8F1F8;
  --ink:#0f172a;
  --text:#475569;
  --muted:#64748b;
  --line:#e5e9f0;
  --bg-alt:#f7f9fc;
  --navy:#111a2e;
  --teal:#2a6b62;
}
*{box-sizing:border-box;margin:0;padding:0}
html,body{width:1200px;height:4018px;overflow:hidden}
body{font-family:"Inter",sans-serif;color:var(--ink);background:#fff}
.serif{font-family:"Playfair Display",serif}
.wrap{padding:0 30px}

.nav{height:75px;display:flex;align-items:center;justify-content:space-between;padding:0 30px;background:#fff;border-bottom:1px solid var(--line)}
.brand{display:flex;align-items:center;gap:10px;font-family:"Playfair Display",serif;font-weight:700;font-size:22px;color:var(--blue)}
.brand-dot{width:20px;height:20px;border-radius:50%;background:var(--blue)}
.nav-links{display:flex;align-items:center;gap:30px;font-size:15px;color:#334155}
.btn-nav{background:var(--blue);color:#fff;padding:11px 19px;border-radius:22px;font-weight:500}

.hero{height:885px;background:linear-gradient(180deg,#5d5a58 0%,#6b6b6c 45%,#7f8386 100%);display:flex;flex-direction:column;align-items:center;padding-top:250px;color:#fff;text-align:center}
.hero h1{font-family:"Playfair Display",serif;font-weight:700;font-size:72px;letter-spacing:.5px;display:flex;align-items:center;gap:22px}
.hero h1 .sep{width:20px;height:20px;border-radius:50%;background:var(--blue-soft)}
.hero p{margin-top:24px;font-size:22px;font-weight:300;line-height:30px;width:590px;color:#eef1f4}
.hero-actions{margin-top:48px;display:flex;gap:16px}
.btn{display:inline-block;border-radius:30px;font-size:16px;font-weight:600;padding:17px 30px}
.btn-primary{background:var(--blue);color:#fff;box-shadow:0 6px 16px rgba(0,40,90,.35)}
.btn-ghost{border:2px solid #fff;color:#fff;padding:15px 30px}

.advisor{height:630px;text-align:center;padding-top:80px}
.eyebrow{font-size:12px;font-weight:600;letter-spacing:1.4px;color:var(--blue);text-transform:uppercase}
.h2{font-family:"Playfair Display",serif;font-weight:700;font-size:34px;margin-top:12px}
.advisor .lead{margin:26px auto 0;width:720px;font-size:16px;line-height:28px;color:var(--text)}
.features{display:flex;gap:30px;margin-top:60px;padding:0 30px;text-align:left}
.feature{flex:1;height:243px;border-top:4px solid var(--blue);border-radius:6px;background:#fff;box-shadow:0 4px 18px rgba(15,23,42,.09);padding:32px 30px}
.icon-box{width:52px;height:50px;border-radius:6px;background:var(--blue-mist);display:flex;align-items:center;justify-content:center}
.feature h3{font-family:"Playfair Display",serif;font-size:19px;font-weight:700;margin-top:26px}
.feature p{margin-top:14px;font-size:14px;line-height:22px;color:var(--text)}

.capabilities{height:765px;background:var(--bg-alt);padding-top:80px;border-bottom:1px solid var(--line)}
.cap-head{display:flex;justify-content:space-between;align-items:flex-end;padding:0 30px}
.cap-head .h2{margin-top:6px}
.link{color:var(--blue);font-size:15px;font-weight:600;padding-bottom:6px}
.grid{display:grid;grid-template-columns:repeat(3,365px);gap:22px 22px;padding:0 30px;margin-top:40px;justify-content:space-between}
.tile{height:240px;border-radius:6px;position:relative;overflow:hidden;box-shadow:0 3px 10px rgba(15,23,42,.12)}
.tile .label{position:absolute;left:24px;top:144px;display:flex;align-items:center;gap:10px;color:#fff;font-size:19px;font-weight:600}
.t-nurse{background:linear-gradient(180deg,#d9d9d9 0%,#8c8c8c 45%,#1c1c1c 100%)}
.t-access{background:linear-gradient(180deg,#1c7068 0%,#0f4f48 50%,#062520 100%)}
.t-wander{background:linear-gradient(180deg,#ece6d6 0%,#a89c7e 50%,#2a251c 100%)}
.t-cctv{background:linear-gradient(180deg,#7cb7d6 0%,#3a6f86 50%,#0e1c24 100%)}
.t-network{background:linear-gradient(180deg,#267a5e 0%,#14513f 50%,#07231b 100%)}
.t-more{background:var(--blue);display:flex;flex-direction:column;align-items:center;justify-content:center;color:#fff;text-align:center}
.t-more h4{font-family:"Playfair Display",serif;font-size:22px;font-weight:700}
.t-more p{margin-top:10px;font-size:15px;color:#dbe8f6}
.pill-white{margin-top:14px;background:#fff;color:var(--blue);font-size:13px;font-weight:600;padding:8px 16px;border-radius:18px}

.about{height:630px;display:flex;padding:0 30px;border-bottom:1px solid var(--line)}
.about-copy{width:540px;padding-top:90px}
.about-copy .h2{font-size:34px;line-height:38px;margin-top:0}
.about-copy p{margin-top:22px;font-size:16px;line-height:28px;color:var(--text)}
.about-copy p+p{margin-top:22px}
.checks{list-style:none;margin-top:22px}
.checks li{display:flex;align-items:center;gap:12px;font-size:15px;color:#1e293b;height:42px}
.about-visual{position:relative;flex:1}
.visual-img{position:absolute;left:60px;top:75px;width:480px;height:480px;border-radius:10px;background:linear-gradient(160deg,#2f7469,#24625a);box-shadow:0 20px 50px rgba(0,84,170,.12)}
.stat{position:absolute;left:38px;top:453px;width:298px;height:125px;background:#fff;border-radius:6px;box-shadow:0 10px 30px rgba(15,23,42,.15);padding:24px 22px}
.stat b{font-family:"Playfair Display",serif;font-size:34px;color:var(--blue);font-weight:700;line-height:34px}
.stat p{margin-top:10px;font-size:13px;line-height:18px;color:var(--text)}

.facilities{height:303px;text-align:center;padding-top:76px}
.facilities .h2{font-size:28px;margin-top:0}
.pills{display:flex;flex-wrap:wrap;justify-content:center;gap:16px;width:1060px;margin:36px auto 0}
.pills span{border:1px solid var(--line);border-radius:24px;padding:14px 22px;font-size:15px;color:#334155;background:#fff;box-shadow:0 1px 3px rgba(15,23,42,.05)}

.cta{height:352px;background:linear-gradient(90deg,#0a5cb1 0%,#0f63b8 40%,#1064b6 60%,#0a5cb1 100%);text-align:center;color:#fff;padding-top:68px}
.cta h2{font-family:"Playfair Display",serif;font-size:34px;font-weight:700}
.cta p{margin:22px auto 0;width:560px;font-size:18px;line-height:27px;color:#dce9f7}
.cta-actions{display:flex;justify-content:center;gap:14px;margin-top:40px}
.cta-btn{display:flex;align-items:center;gap:10px;height:54px;padding:0 30px;border-radius:4px;font-size:15px;font-weight:600}
.cta-phone{background:#fff;color:var(--blue)}
.cta-mail{background:var(--blue-2);color:#fff}

.footer{height:378px;background:var(--navy);color:#aab3c5;padding:60px 30px 0;position:relative}
.foot-cols{display:grid;grid-template-columns:296px 296px 296px 1fr;font-size:13px}
.footer .brand{color:#fff}
.foot-about{margin-top:24px;line-height:21px;width:250px}
.socials{display:flex;gap:14px;margin-top:22px}
.socials i{width:18px;height:18px;border-radius:50%;background:#6b7588;display:block}
.foot-col h5{color:#fff;font-size:13px;font-weight:600;letter-spacing:1px;margin-top:8px}
.foot-col ul{list-style:none;margin-top:24px}
.foot-col li{margin-bottom:14px;color:#c4cad6}
.contact li{display:flex;gap:14px;line-height:19px;margin-bottom:16px}
.copyright{position:absolute;left:0;right:0;bottom:42px;text-align:center;font-size:12px;color:#6b7588;border-top:1px solid #1f2a40;padding-top:0}
</style>
</head>
<body>

<header class="nav">
  <div class="brand"><span class="brand-dot"></span>Velmora</div>
  <nav class="nav-links">
    <span>Solutions</span><span>Facilities</span><span>About Us</span>
    <span class="btn-nav">Contact Us</span>
  </nav>
</header>

<section class="hero" role="img" aria-label="Softly lit photograph of a senior living interior behind the headline">
  <h1>Design<span class="sep"></span>Install<span class="sep"></span>Maintain</h1>
  <p>Supporting the safety and security needs of your community. Best in class systems for the safety of your residents and staff.</p>
  <div class="hero-actions">
    <span class="btn btn-primary">Explore Solutions</span>
    <span class="btn btn-ghost">Request Consultation</span>
  </div>
</section>

<section class="advisor">
  <div class="eyebrow">Your Trusted Advisor</div>
  <h2 class="h2">Systems Tailored to Your Facility</h2>
  <p class="lead">Velmora specializes in the design, installation, and maintenance of low voltage systems including Nurse Call, Delayed Egress, Network Infrastructure, and Overhead Paging primarily for healthcare clients and senior living communities.</p>
  <div class="features">
    <div class="feature">
      <div class="icon-box"><svg width="22" height="22" viewBox="0 0 24 24"><rect x="3" y="7" width="18" height="13" rx="2" fill="#0054AA"/><rect x="9" y="4" width="6" height="4" rx="1" fill="none" stroke="#0054AA" stroke-width="2"/><path d="M12 10v7M8.5 13.5h7" stroke="#fff" stroke-width="2"/></svg></div>
      <h3>Healthcare Specialized</h3>
      <p>Tailored solutions for Skilled Nursing, Assisted Living, Memory Care, and Outpatient Surgical Centers.</p>
    </div>
    <div class="feature">
      <div class="icon-box"><svg width="22" height="22" viewBox="0 0 24 24"><rect x="3" y="6" width="18" height="14" rx="2" fill="#0054AA"/><rect x="8" y="3" width="8" height="4" rx="1" fill="#0054AA"/><path d="M10 10l-2 3 2 3M14 10l2 3-2 3" stroke="#fff" stroke-width="1.8" fill="none"/></svg></div>
      <h3>Integrated Systems</h3>
      <p>Seamless integration of Nurse Call, Access Control, Wander Management, and Wireless Networks.</p>
    </div>
    <div class="feature">
      <div class="icon-box"><svg width="22" height="22" viewBox="0 0 24 24"><path d="M12 2l8 3v6c0 5-3.5 9-8 11-4.5-2-8-6-8-11V5z" fill="#0054AA"/><path d="M8 12l3 3 5-6" stroke="#fff" stroke-width="2" fill="none"/></svg></div>
      <h3>Resident Safety</h3>
      <p>Advanced detection, alarming, and remote monitoring to ensure the highest standard of care and security.</p>
    </div>
  </div>
</section>

<section class="capabilities">
  <div class="cap-head">
    <div>
      <div class="eyebrow">Our Capabilities</div>
      <h2 class="h2">Comprehensive Safety Solutions</h2>
    </div>
    <span class="link">View full capabilities →</span>
  </div>
  <div class="grid">
    <div class="tile t-nurse" role="img" aria-label="Photo of a wall-mounted nurse call station">
      <span class="label"><svg width="18" height="18" viewBox="0 0 24 24"><path d="M12 3a6 6 0 0 0-6 6v5l-2 3h16l-2-3V9a6 6 0 0 0-6-6zM10 19a2 2 0 0 0 4 0" fill="#7BADD7"/></svg>Nurse Call</span>
    </div>
    <div class="tile t-access" role="img" aria-label="Photo of an access control keypad">
      <span class="label"><svg width="16" height="18" viewBox="0 0 24 24"><rect x="4" y="10" width="16" height="11" rx="2" fill="#CADEEF"/><path d="M8 10V7a4 4 0 0 1 8 0v3" stroke="#CADEEF" stroke-width="2.4" fill="none"/></svg>Access Control</span>
    </div>
    <div class="tile t-wander" role="img" aria-label="Photo of a wander management device beside a plant">
      <span class="label"><svg width="16" height="18" viewBox="0 0 24 24"><circle cx="13" cy="4" r="2.2" fill="#7BADD7"/><path d="M12 8l-3 5 3 2-1 7M12 8l3 4 3 1M9 13l-3 1" stroke="#7BADD7" stroke-width="2.2" fill="none"/></svg>Wander Management</span>
    </div>
    <div class="tile t-cctv" role="img" aria-label="Photo of a ceiling-mounted security camera">
      <span class="label"><svg width="18" height="16" viewBox="0 0 24 24"><rect x="2" y="6" width="14" height="12" rx="2" fill="#7BADD7"/><path d="M16 10l6-3v10l-6-3z" fill="#7BADD7"/></svg>CCTV Surveillance</span>
    </div>
    <div class="tile t-network" role="img" aria-label="Illustration of a glowing network of connected nodes">
      <span class="label"><svg width="18" height="16" viewBox="0 0 24 24"><rect x="2" y="14" width="20" height="7" rx="1" fill="#CADEEF"/><path d="M12 4v10M7 7v7M17 7v7" stroke="#CADEEF" stroke-width="2"/></svg>Network Infrastructure</span>
    </div>
    <div class="tile t-more">
      <h4>And More</h4>
      <p>Conference, Telepresence, Hybrid Systems</p>
      <span class="pill-white">View All Services</span>
    </div>
  </div>
</section>

<section class="about">
  <div class="about-copy">
    <h2 class="h2">Revolutionizing Integrated<br>Systems</h2>
    <p>Velmora was founded to fill a specific need. Senior living communities and healthcare facilities of all kinds face unique challenges in regards to technology and systems integration.</p>
    <p>We are perfectly positioned with an experienced management team, skilled technicians, and industry relationships to deliver innovative, reliable, tailored solutions that enhance operational efficiency.</p>
    <ul class="checks">
      <li><svg width="20" height="20" viewBox="0 0 24 24"><circle cx="12" cy="12" r="10" fill="#22a55a"/><path d="M7 12l3.5 3.5L17 9" stroke="#fff" stroke-width="2.4" fill="none"/></svg>Excellent Customer Service</li>
      <li><svg width="20" height="20" viewBox="0 0 24 24"><circle cx="12" cy="12" r="10" fill="#22a55a"/><path d="M7 12l3.5 3.5L17 9" stroke="#fff" stroke-width="2.4" fill="none"/></svg>Highest Standards of Integrity</li>
      <li><svg width="20" height="20" viewBox="0 0 24 24"><circle cx="12" cy="12" r="10" fill="#22a55a"/><path d="M7 12l3.5 3.5L17 9" stroke="#fff" stroke-width="2.4" fill="none"/></svg>Industry Expertise &amp; Innovation</li>
    </ul>
  </div>
  <div class="about-visual">
    <div class="visual-img" role="img" aria-label="Teal panel with a technology themed illustration"></div>
    <div class="stat">
      <b>100%</b>
      <p>Commitment to setting new standards for resident safety.</p>
    </div>
  </div>
</section>

<section class="facilities">
  <h2 class="h2">Facilities We Serve</h2>
  <div class="pills">
    <span>Independent Senior Living</span><span>Assisted Living</span><span>Memory Care</span><span>CCRC</span><span>Skilled Nursing / Rehab</span><span>Acute Care</span><span>Commercial Properties</span>
  </div>
</section>

<section class="cta">
  <h2>Ready to upgrade your facility's safety?</h2>
  <p>Contact our team for a consultation on good, better, and best proposals tailored to your budget and needs.</p>
  <div class="cta-actions">
    <span class="cta-btn cta-phone"><svg width="18" height="18" viewBox="0 0 24 24"><path d="M6.6 10.8a15 15 0 0 0 6.6 6.6l2.2-2.2c.3-.3.7-.4 1-.2 1.1.4 2.3.6 3.6.6.6 0 1 .4 1 1V20c0 .6-.4 1-1 1A17 17 0 0 1 3 4c0-.6.4-1 1-1h3.5c.6 0 1 .4 1 1 0 1.3.2 2.5.6 3.6.1.3 0 .7-.2 1z" fill="#0054AA"/></svg>(603) 555-0172</span>
    <span class="cta-btn cta-mail"><svg width="20" height="16" viewBox="0 0 24 20"><rect x="1" y="2" width="22" height="16" rx="2" fill="#fff"/><path d="M2 4l10 7 10-7" stroke="#0677BA" stroke-width="2" fill="none"/></svg>Email Us</span>
  </div>
</section>

<footer class="footer">
  <div class="foot-cols">
    <div>
      <div class="brand"><span class="brand-dot"></span>Velmora</div>
      <p class="foot-about">Revolutionizing integrated systems within healthcare and commercial environments by delivering innovative, reliable, and tailored solutions.</p>
      <div class="socials"><i></i><i></i></div>
    </div>
    <div class="foot-col">
      <h5>COMPANY</h5>
      <ul><li>About Us</li><li>Our Team</li><li>Careers</li><li>Privacy Policy</li></ul>
    </div>
    <div class="foot-col">
      <h5>SERVICES</h5>
      <ul><li>Nurse Call Systems</li><li>Access Control</li><li>Wander Management</li><li>CCTV Surveillance</li><li>Network Infrastructure</li></ul>
    </div>
    <div class="foot-col contact">
      <h5>CONTACT</h5>
      <ul>
        <li><svg width="12" height="16" viewBox="0 0 24 32"><path d="M12 0a12 12 0 0 0-12 12c0 9 12 20 12 20s12-11 12-20A12 12 0 0 0 12 0z" fill="#0677BA"/><circle cx="12" cy="12" r="4" fill="#111a2e"/></svg><span>Harborline Collective<br>Massachusetts Chapter</span></li>
        <li><svg width="14" height="14" viewBox="0 0 24 24"><path d="M6.6 10.8a15 15 0 0 0 6.6 6.6l2.2-2.2c.3-.3.7-.4 1-.2 1.1.4 2.3.6 3.6.6.6 0 1 .4 1 1V20c0 .6-.4 1-1 1A17 17 0 0 1 3 4c0-.6.4-1 1-1h3.5c.6 0 1 .4 1 1 0 1.3.2 2.5.6 3.6.1.3 0 .7-.2 1z" fill="#0677BA"/></svg><span>(603) 555-0172</span></li>
        <li><svg width="14" height="12" viewBox="0 0 24 20"><rect x="1" y="2" width="22" height="16" rx="2" fill="#0677BA"/><path d="M2 4l10 7 10-7" stroke="#111a2e" stroke-width="2" fill="none"/></svg><span>Info@Velmora.example</span></li>
      </ul>
    </div>
  </div>
  <div class="copyright">© 2023 Velmora. All rights reserved.</div>
</footer>

</body>
</html>
```